"End of year wishes" - Electronic card

Velmora is a regulatory consulting company in the cosmetic sector. We provide premium services and have 12 years of experience.
Please visit our website for more information: https://velmora-example.com
Like every year, we would like to send an electronic design to our clients and partners to wish them happy holidays. This year, we would like to share two good news with them: offer them a surprise (to be revealed later on) and invite them to visit our new brand new website. We relay on your talent and imagination for the design! We need something very professional, serious, beautiful and in line with our graphic layout (see our company website)

Target Market(s)

cosmetic brands

Industry/Entity Type

Cosmetics

Requirements
Must have
• The following statement should be included to the design:

We wish you a Happy Holiday and a Marvelous New Year 2021!
As December is the month of giving, we have a surprise for you. Please contact your dedicated Account Manager to find out more!

Good news never comes alone, we've also updated our website in order to serve you better. We hope you like it as much as we do.
Please enjoy the experience: www.velmora-example.com

```html
<!DOCTYPE html>
<html lang="en">
<head>
<meta charset="utf-8">
<title>Velmora – Season's Greetings 2021</title>
<link rel="stylesheet" href="https://fonts.googleapis.com/css2?family=Montserrat:ital,wght@0,400;0,500;0,600;0,700;1,500;1,600&display=swap">
<style>
  :root {
    --night: #151515;
    --night-deep: #0b0b0b;
    --lime: #8cc63f;
    --lime-bright: #9bd32b;
    --paper: #ffffff;
    --ink: #3a3a3a;
    --ink-dark: #222222;
  }
  * { box-sizing: border-box; margin: 0; padding: 0; }
  html, body { width: 900px; height: 1200px; overflow: hidden; background: var(--paper); }
  body { font-family: "Montserrat", Arial, sans-serif; }

  .ecard {
    position: relative;
    width: 900px;
    height: 1200px;
    overflow: hidden;
    background: var(--paper);
  }

  .night-sky {
    position: absolute;
    left: 0; top: 0;
    width: 900px; height: 800px;
  }

  .ornament-garland {
    position: absolute;
    left: 0; top: 0;
    width: 900px; height: 380px;
    background:
      radial-gradient(circle at 120px 200px, rgba(140,198,63,0.22) 0 75px, transparent 80px),
      radial-gradient(circle at 330px 120px, rgba(140,198,63,0.18) 0 45px, transparent 50px),
      radial-gradient(circle at 480px 260px, rgba(140,198,63,0.22) 0 75px, transparent 80px),
      radial-gradient(circle at 640px 70px, rgba(140,198,63,0.18) 0 45px, transparent 50px),
      radial-gradient(circle at 810px 160px, rgba(140,198,63,0.22) 0 65px, transparent 70px);
  }

  .greeting {
    position: absolute;
    left: 0; top: 462px;
    width: 900px;
    text-align: center;
    color: var(--paper);
    font-weight: 600;
    font-size: 40px;
    line-height: 60px;
  }
  .greeting .highlight { color: var(--lime-bright); }

  .surprise {
    position: absolute;
    left: 0; top: 636px;
    width: 900px;
    padding: 0 105px;
    text-align: center;
    color: var(--paper);
    font-weight: 500;
    font-size: 22px;
    line-height: 32px;
  }
  .surprise em { font-style: italic; font-weight: 600; }

  .website-news {
    position: absolute;
    left: 0; top: 862px;
    width: 900px;
    padding: 0 66px;
    color: var(--ink);
    font-size: 22px;
    line-height: 34px;
    text-align: justify;
  }
  .website-news strong { color: var(--ink-dark); font-weight: 700; }

  .website-button {
    position: absolute;
    left: 240px; top: 976px;
    width: 420px; height: 62px;
    background: var(--lime);
    color: var(--paper);
    font-weight: 700;
    font-size: 24px;
    line-height: 62px;
    text-align: center;
    text-decoration: none;
  }

  .brand {
    position: absolute;
    left: 0; top: 1066px;
    width: 900px;
    display: flex;
    justify-content: center;
    align-items: center;
    gap: 8px;
  }
  .brand-name {
    font-weight: 600;
    font-size: 30px;
    color: var(--ink-dark);
    letter-spacing: 0.5px;
  }
  .brand-dot {
    width: 9px; height: 9px;
    border-radius: 50%;
    background: var(--lime);
  }
</style>
</head>
<body>
  <main class="ecard">
    <svg class="night-sky" width="900" height="800" viewBox="0 0 900 800" aria-hidden="true">
      <defs>
        <linearGradient id="sky-gradient" x1="0" y1="0" x2="0" y2="1">
          <stop offset="0" stop-color="#1d1d1d"/>
          <stop offset="1" stop-color="#0e0e0e"/>
        </linearGradient>
      </defs>
      <rect x="0" y="0" width="900" height="800" fill="#8cc63f"/>
      <polygon points="0,0 900,0 900,596 0,618" fill="url(#sky-gradient)"/>
    </svg>

    <div class="ornament-garland" role="img" aria-label="Hanging outline holiday baubles with snowflakes and stars on a starry night sky"></div>

    <h1 class="greeting">
      We wish you a <span class="highlight">Happy Holiday</span><br>
      and a <span class="highlight">Marvelous New Year 2021!</span>
    </h1>

    <p class="surprise">
      As <em>December</em> is the month of <em>giving</em>, we have a surprise for you. Please <em>contact</em> your dedicated <em>Account Manager</em> to find out more!
    </p>

    <p class="website-news">
      <strong>Good news</strong> never comes alone, we've also <strong>updated</strong> our website in order to serve you better. We hope you like it as much as we do. Please enjoy the experience.
    </p>

    <a class="website-button" href="https://velmora-example.com">www.velmora-example.com</a>

    <div class="brand">
      <span class="brand-name">velmora</span>
      <span class="brand-dot"></span>
    </div>
  </main>
</body>
</html>
```